Letterhead for Conveyancing Company

Use existing logo to create a letterhead for a conveyancing company. Must be able to be used in Microsoft Word. Easy to read and professional.
Contact information to be at the bottom.
Bright Wren Conveyancing Pty Ltd
ACN 621 984 736PO Box 535 Campbelltown SA 5074
Mobile - 0461273985
Web address - www.brightwrenconveyancing.com.au

Requirements
Must have
• Logo and contact details.
• Simple and professional.

```html
<!DOCTYPE html>
<html lang="en">
<head>
<meta charset="utf-8">
<title>Bright Wren Conveyancing – Letterhead</title>
<link href="https://fonts.googleapis.com/css2?family=PT+Sans:wght@400;700&display=swap" rel="stylesheet">
<style>
  :root {
    --brand-pink: #f52af4;
    --brand-grey: #7a8b89;
    --watermark: #eef1f1;
    --paper: #ffffff;
  }
  * { margin: 0; padding: 0; box-sizing: border-box; }
  html, body { width: 873px; height: 1200px; overflow: hidden; background: var(--paper); }
  .letterhead {
    position: relative;
    width: 873px;
    height: 1200px;
    background: var(--paper);
    font-family: "PT Sans", Arial, sans-serif;
  }
  .brand-name {
    position: absolute;
    left: 48px;
    top: 18px;
    width: 200px;
    color: var(--brand-grey);
    font-weight: 700;
    font-size: 30px;
    line-height: 30px;
  }
  .brand-mark {
    display: inline-block;
    width: 14px;
    height: 14px;
    background: var(--brand-pink);
    margin-left: 6px;
    vertical-align: middle;
  }
  .band { position: absolute; }
  .band--top-pink { left: 286px; top: 10px; width: 587px; height: 29px; background: var(--brand-pink); }
  .band--top-grey { left: 286px; top: 51px; width: 587px; height: 44px; background: var(--brand-grey); }
  .band--foot-grey { left: 0; top: 1115px; width: 424px; height: 43px; background: var(--brand-grey); }
  .band--foot-pink { left: 0; top: 1171px; width: 424px; height: 29px; background: var(--brand-pink); }
  .watermark-name {
    position: absolute;
    left: 236px;
    top: 540px;
    width: 400px;
    text-align: center;
    color: var(--watermark);
    font-weight: 700;
    font-size: 64px;
    line-height: 66px;
  }
  .footer-details {
    position: absolute;
    left: 440px;
    top: 1116px;
    width: 420px;
    text-align: center;
  }
  .footer-details__company { color: var(--brand-pink); font-size: 15.5px; line-height: 20px; }
  .footer-details__registry { color: var(--brand-grey); font-size: 14.5px; line-height: 20px; }
  .footer-details__registry .divider { color: var(--brand-pink); margin: 0 7px; }
  .footer-contacts {
    margin-top: 15px;
    display: flex;
    justify-content: center;
    gap: 12px;
    color: var(--brand-grey);
    font-size: 15px;
    line-height: 18px;
  }
  .contact { display: flex; align-items: center; gap: 3px; }
  .contact svg { width: 17px; height: 17px; flex: none; }
</style>
</head>
<body>
  <div class="letterhead">
    <div class="brand-name">Bright Wren<span class="brand-mark"></span></div>
    <div class="band band--top-pink"></div>
    <div class="band band--top-grey"></div>

    <div class="watermark-name" aria-hidden="true">Bright Wren</div>

    <div class="band band--foot-grey"></div>
    <div class="band band--foot-pink"></div>

    <div class="footer-details">
      <p class="footer-details__company">Bright Wren Conveyancing Pty Ltd.</p>
      <p class="footer-details__registry">ACN 738 215 490<span class="divider">|</span>PO Box 862 Marlow Heights SA 5093</p>
      <div class="footer-contacts">
        <span class="contact">
          <svg viewBox="0 0 20 20" aria-hidden="true">
            <circle cx="10" cy="10" r="10" fill="var(--brand-pink)"/>
            <rect x="6.5" y="4" width="7" height="12" rx="1.5" fill="#fff"/>
            <rect x="7.8" y="5.5" width="4.4" height="8.5" fill="var(--brand-pink)"/>
          </svg>
          0461273985
        </span>
        <span class="contact">
          <svg viewBox="0 0 20 20" aria-hidden="true">
            <circle cx="10" cy="10" r="10" fill="var(--brand-pink)"/>
            <g fill="none" stroke="#fff" stroke-width="1">
              <circle cx="10" cy="10" r="7"/>
              <ellipse cx="10" cy="10" rx="3" ry="7"/>
              <line x1="3" y1="10" x2="17" y2="10"/>
              <line x1="10" y1="3" x2="10" y2="17"/>
              <line x1="4.5" y1="6.5" x2="15.5" y2="6.5"/>
              <line x1="4.5" y1="13.5" x2="15.5" y2="13.5"/>
            </g>
          </svg>
          www.brightwrenconveyancing.com.au
        </span>
      </div>
    </div>
  </div>
</body>
</html>
```